Architecture firm needing a business card

We need a business card design for a new company based in the US called "Pellmore Architecture". Seeking minimalist designs that have a creativity/design feel but must be clean and professional. Please refer to the logo attached.

Target Market(s)

Real Estate Investors, Home Builders and Construction Firms.

Industry/Entity Type

Architecture

Contact Information for Business Card

Standard US size business cards. Would like to have some sort of graphic on the back side of the card - nothing that is too loud but something that may catch your attention. More or less grayscale colors that are in line with the logo colors (navy and greys essentially). Additional colors maybe accepted if blended properly (earthtones), but might be difficult to accomplish and maintain the clean/minimalist look.

Requirements
Must have
• Clean Lines
Nice to have
• some sort of graphics, would like to have something creative on the back side of the card
Should not have
• nothing too busy, cluttered or overwhelming.

```html
<!DOCTYPE html>
<html lang="en">
<head>
<meta charset="utf-8">
<title>Pellmore Architecture — Business Card</title>
<link rel="stylesheet" href="https://fonts.googleapis.com/css2?family=Open+Sans:wght@400;600&display=swap">
<style>
  :root {
    --page: #ffffff;
    --front-dark: #1d5f9c;
    --front-mid: #146f9f;
    --front-light: #0b88a6;
    --ink-light: #ffffff;
    --mark-grey: #a9b6c4;
    --back-dark: #5c5e60;
    --back-mid: #8a8c8e;
    --back-light: #a4a5a6;
    --navy: #1f3f66;
  }
  * { margin: 0; padding: 0; box-sizing: border-box; }
  html, body {
    width: 1200px; height: 336px; overflow: hidden;
    background: var(--page);
    font-family: "Open Sans", Arial, sans-serif;
  }
  .canvas { position: relative; width: 1200px; height: 336px; }

  .card-front {
    position: absolute; left: 0; top: 0; width: 588px; height: 336px;
    background: linear-gradient(90deg, var(--front-dark) 0%, var(--front-mid) 50%, var(--front-light) 100%);
    color: var(--ink-light);
  }
  .contact {
    position: absolute; left: 40px; top: 80px; width: 250px;
    text-align: center; font-size: 17px; line-height: 25px;
  }
  .contact .gap { height: 20px; }

  .wordmark {
    position: absolute; display: flex; align-items: center; gap: 10px;
    font-weight: 600; letter-spacing: 2px;
  }
  .wordmark .square { width: 34px; height: 34px; }
  .wordmark .name { line-height: 1.05; }
  .wordmark .name span { display: block; }
  .wordmark .name .first { font-size: 24px; }
  .wordmark .name .second { font-size: 10.5px; letter-spacing: 3px; }

  .card-front .wordmark { left: 286px; top: 128px; color: var(--mark-grey); }
  .card-front .wordmark .square { border: 3px solid var(--mark-grey); }

  .dimensions { position: absolute; left: 0; top: 0; }
  .dimensions text { font-family: "Open Sans", Arial, sans-serif; font-size: 10px; fill: var(--ink-light); }

  .card-back {
    position: absolute; left: 660px; top: 0; width: 540px; height: 336px;
    background: linear-gradient(180deg, var(--back-light) 0%, var(--back-mid) 45%, var(--back-dark) 100%);
    overflow: hidden;
  }
  .back-artwork {
    position: absolute; inset: 0;
    background: radial-gradient(ellipse at 45% 40%, rgba(160,120,80,0.35) 0%, rgba(0,0,0,0) 55%);
  }
  .card-back .wordmark { left: 280px; top: 206px; color: var(--navy); }
  .card-back .wordmark .square { border: 3px solid var(--navy); }
</style>
</head>
<body>
<div class="canvas">

  <section class="card-front">
    <div class="contact">
      <p>480 Quarry Lane</p>
      <p>Henderson, NV 89012</p>
      <p>Phone: 702-555-0148</p>
      <div class="gap"></div>
      <p>email : hello@pellmore.com</p>
      <p>website: www.pellmore.com</p>
    </div>

    <div class="wordmark">
      <div class="square"></div>
      <div class="name"><span class="first">PELLMORE</span><span class="second">ARCHITECTURE</span></div>
    </div>

    <svg class="dimensions" width="588" height="336" viewBox="0 0 588 336" aria-hidden="true">
      <g stroke="#ffffff" stroke-width="2" fill="none">
        <line x1="486" y1="22" x2="486" y2="306"/>
        <polyline points="478,32 486,20 494,32"/>
        <polyline points="478,296 486,308 494,296"/>
        <line x1="22" y1="276" x2="470" y2="276"/>
        <polyline points="32,268 20,276 32,284"/>
        <polyline points="460,268 472,276 460,284"/>
      </g>
      <text x="492" y="184">1.75"</text>
      <text x="240" y="296">2.5"</text>
    </svg>
  </section>

  <section class="card-back">
    <div class="back-artwork" role="img" aria-label="Photograph of two pencil tips carved into reaching hands against a grey backdrop"></div>
    <div class="wordmark">
      <div class="square"></div>
      <div class="name"><span class="first">PELLMORE</span><span class="second">ARCHITECTURE</span></div>
    </div>
  </section>

</div>
</body>
</html>
```